I need email signatures for my admin staff members
info:
Darina Qubrosi
Support Coordinator
Unit 4, 517 Wattlebrook Lane, Kemberly NSW 2893
Tel: 02 84427193 Mob: 0427596314
email: darina.qu@mivrotelhaven.com
www.mivrotelhaven.com

Target Market(s)

community services industry

Industry/Entity Type

Community Service

Requirements
Must have
• Specialist Provider of Multicultural Support Services
Nice to have
• "I acknowledge the traditional owners of the land on which we live, work and dream"
plus their flags as attached

```html
<!DOCTYPE html>
<html lang="en">
<head>
<meta charset="utf-8">
<title>Email Signatures – Darina Qubrosi</title>
<link rel="stylesheet" href="https://fonts.googleapis.com/css2?family=Catamaran:wght@400;500;600;700&display=swap">
<style>
:root{
  --orange:#ff8108;
  --dark:#21282a;
  --white:#ffffff;
  --ink:#1d1d1f;
  --page:#ffffff;
}
*{box-sizing:border-box;margin:0;padding:0}
html,body{width:1200px;height:1000px;overflow:hidden;background:var(--page);font-family:"Catamaran",sans-serif}
.signature{position:absolute;left:54px;width:1097px;height:364px;overflow:hidden;box-shadow:0 3px 10px rgba(0,0,0,.18)}
.signature--dark{top:117px;background:var(--dark);color:var(--white)}
.signature--light{top:519px;background:var(--white);color:var(--ink)}
.shapes{position:absolute;inset:0}
.portrait{position:absolute;left:299px;top:86px;width:176px;height:176px;border-radius:50%;
  background:radial-gradient(circle at 50% 70%,#e9e2dc 0 22%,#6d5a52 40%,#3d3a44 70%,#8a8496 100%)}
.person{position:absolute;z-index:1}
.person__name{font-size:29px;font-weight:600;color:var(--orange);line-height:1;white-space:nowrap}
.person__role{font-size:14px;font-weight:600;letter-spacing:3.6px;margin-top:8px;white-space:nowrap}
.contacts{position:absolute;list-style:none;z-index:1}
.contacts li{display:flex;align-items:center;height:35px;font-size:18.5px;font-weight:500;white-space:nowrap}
.contacts li.address{height:auto;line-height:22px;align-items:flex-start;margin-top:4px}
.contacts svg{width:24px;height:24px;margin-right:16px;flex:none;fill:var(--orange)}
.brand{position:absolute;text-align:center;width:200px}
.brand__mark{width:74px;height:74px;border-radius:50%;margin:0 auto 8px}
.brand__name{font-size:21px;font-weight:600;letter-spacing:1px;line-height:1}
.tagline{position:absolute;font-size:14.5px;font-weight:500;line-height:17px;text-align:right}
.acknowledgement{position:absolute;font-weight:600;line-height:21px;z-index:1}
.social{position:absolute;display:flex;align-items:center;gap:8px}
.social__menu{width:20px;height:20px;margin-right:8px;
  background:radial-gradient(circle,currentColor 0 2.6px,transparent 3px) 0 0/6.7px 6.7px}
.social__item{width:22px;height:22px;border-radius:5px;background:var(--orange)}
</style>
</head>
<body>

<section class="signature signature--dark">
  <svg class="shapes" viewBox="0 0 1097 364" aria-hidden="true">
    <rect x="0" y="0" width="300" height="235" fill="var(--orange)"/>
    <circle cx="165" cy="200" r="140" fill="var(--dark)"/>
    <circle cx="248" cy="20" r="52" fill="var(--dark)"/>
    <rect x="248" y="0" width="60" height="72" fill="var(--dark)"/>
    <circle cx="387" cy="174" r="148" fill="var(--dark)"/>
    <circle cx="387" cy="174" r="138" fill="none" stroke="var(--orange)" stroke-width="20"/>
    <circle cx="387" cy="174" r="108" fill="none" stroke="var(--orange)" stroke-width="12" stroke-linecap="round" stroke-dasharray="0 30 150 170 170 400" transform="rotate(-5 387 174)"/>
    <rect x="0" y="251" width="318" height="3" fill="var(--orange)"/>
    <rect x="520" y="251" width="300" height="3" fill="var(--orange)"/>
    <path d="M550 364 A62 62 0 0 1 612 302 H1097 V364 Z" fill="var(--orange)"/>
    <circle cx="1056" cy="46" r="33" fill="var(--orange)"/>
    <circle cx="996" cy="48" r="32" fill="var(--orange)"/>
    <circle cx="1086" cy="95" r="22" fill="var(--orange)"/>
  </svg>
  <div class="portrait" role="img" aria-label="Portrait photo of Darina Qubrosi"></div>

  <div class="person" style="left:21px;top:195px">
    <h1 class="person__name">Darina Qubrosi</h1>
    <p class="person__role">SUPPORT COORDINATOR</p>
  </div>

  <ul class="contacts" style="left:548px;top:29px">
    <li><svg viewBox="0 0 24 24"><path d="M6.6 10.8a15 15 0 0 0 6.6 6.6l2.2-2.2c.3-.3.7-.4 1-.2 1.1.4 2.3.6 3.6.6.6 0 1 .4 1 1V20c0 .6-.4 1-1 1A17 17 0 0 1 3 4c0-.6.4-1 1-1h3.5c.6 0 1 .4 1 1 0 1.3.2 2.5.6 3.6.1.3 0 .7-.2 1z"/></svg>02 84427193</li>
    <li><svg viewBox="0 0 24 24"><path d="M7 1h10a2 2 0 0 1 2 2v18a2 2 0 0 1-2 2H7a2 2 0 0 1-2-2V3a2 2 0 0 1 2-2zm0 3v15h10V4z"/></svg>0427596314</li>
    <li><svg viewBox="0 0 24 24"><path d="M1 5h22v14H1zm2 2v.4l9 6 9-6V7zm0 2.8V17h18V9.8l-9 6z"/></svg>darina.qu@mivrotelhaven.com</li>
    <li><svg viewBox="0 0 24 24"><path d="M12 2a10 10 0 1 0 0 20 10 10 0 0 0 0-20zm-1 2.1V8H7.3A8 8 0 0 1 11 4.1zm2 0A8 8 0 0 1 16.7 8H13zM6.3 10H11v4H6.3a8 8 0 0 1 0-4zm6.7 0h4.7a8 8 0 0 1 0 4H13zm-5.7 6H11v3.9A8 8 0 0 1 7.3 16zm5.7 0h3.7a8 8 0 0 1-3.7 3.9z"/></svg>www.mivrotelhaven.com</li>
    <li class="address"><svg viewBox="0 0 24 24"><path d="M12 1a8 8 0 0 0-8 8c0 6 8 14 8 14s8-8 8-14a8 8 0 0 0-8-8zm0 11a3 3 0 1 1 0-6 3 3 0 0 1 0 6z"/></svg><span>Unit 4, 517 Wattlebrook Lane,<br>Kemberly NSW 2893</span></li>
  </ul>

  <div class="brand" style="left:885px;top:106px">
    <div class="brand__mark" style="background:var(--white)"></div>
    <p class="brand__name">MIVROTEL HAVEN</p>
  </div>
  <p class="tagline" style="right:14px;top:243px">Specialist Provider of Multicultural<br>Support Services</p>
  <p class="acknowledgement" style="right:28px;top:310px;font-size:19px;text-align:right;color:var(--white)">“I acknowledge the traditional owners of the land<br>on which we live, work and dream"</p>

  <div class="social" style="left:20px;top:318px;color:var(--white)">
    <span class="social__menu"></span>
    <span class="social__item"></span><span class="social__item"></span><span class="social__item"></span><span class="social__item"></span>
  </div>
</section>

<section class="signature signature--light">
  <svg class="shapes" viewBox="0 0 1097 364" aria-hidden="true">
    <rect x="0" y="0" width="300" height="252" fill="var(--orange)"/>
    <circle cx="116" cy="148" r="118" fill="var(--white)"/>
    <rect x="0" y="148" width="116" height="104" fill="var(--white)"/>
    <circle cx="246" cy="22" r="50" fill="var(--white)"/>
    <rect x="246" y="0" width="62" height="72" fill="var(--white)"/>
    <circle cx="387" cy="174" r="148" fill="var(--white)"/>
    <circle cx="387" cy="174" r="138" fill="none" stroke="var(--orange)" stroke-width="20"/>
    <circle cx="387" cy="174" r="108" fill="none" stroke="var(--orange)" stroke-width="12" stroke-linecap="round" stroke-dasharray="0 30 150 170 170 400" transform="rotate(-5 387 174)"/>
    <rect x="0" y="251" width="318" height="3" fill="var(--orange)"/>
    <rect x="520" y="103" width="305" height="3" fill="var(--orange)"/>
    <circle cx="988" cy="292" r="62" fill="var(--orange)"/>
    <circle cx="1058" cy="262" r="44" fill="var(--orange)"/>
    <rect x="1000" y="300" width="97" height="64" fill="var(--orange)"/>
  </svg>
  <div class="portrait" role="img" aria-label="Portrait photo of Darina Qubrosi"></div>

  <p class="acknowledgement" style="left:1px;top:118px;width:232px;font-size:18.5px;text-align:center;color:var(--orange)">“I acknowledge<br>the traditional owners<br>of the land<br>on which we live,<br>work and dream"</p>

  <div class="person" style="left:520px;top:44px;text-align:right;width:303px">
    <h1 class="person__name">Darina Qubrosi</h1>
    <p class="person__role">SUPPORT COORDINATOR</p>
  </div>

  <ul class="contacts" style="left:560px;top:125px;color:var(--ink)">
    <li><svg viewBox="0 0 24 24"><path d="M6.6 10.8a15 15 0 0 0 6.6 6.6l2.2-2.2c.3-.3.7-.4 1-.2 1.1.4 2.3.6 3.6.6.6 0 1 .4 1 1V20c0 .6-.4 1-1 1A17 17 0 0 1 3 4c0-.6.4-1 1-1h3.5c.6 0 1 .4 1 1 0 1.3.2 2.5.6 3.6.1.3 0 .7-.2 1z"/></svg>02 84427193</li>
    <li><svg viewBox="0 0 24 24"><path d="M7 1h10a2 2 0 0 1 2 2v18a2 2 0 0 1-2 2H7a2 2 0 0 1-2-2V3a2 2 0 0 1 2-2zm0 3v15h10V4z"/></svg>0427596314</li>
    <li><svg viewBox="0 0 24 24"><path d="M1 5h22v14H1zm2 2v.4l9 6 9-6V7zm0 2.8V17h18V9.8l-9 6z"/></svg>darina.qu@mivrotelhaven.com</li>
    <li><svg viewBox="0 0 24 24"><path d="M12 2a10 10 0 1 0 0 20 10 10 0 0 0 0-20zm-1 2.1V8H7.3A8 8 0 0 1 11 4.1zm2 0A8 8 0 0 1 16.7 8H13zM6.3 10H11v4H6.3a8 8 0 0 1 0-4zm6.7 0h4.7a8 8 0 0 1 0 4H13zm-5.7 6H11v3.9A8 8 0 0 1 7.3 16zm5.7 0h3.7a8 8 0 0 1-3.7 3.9z"/></svg>www.mivrotelhaven.com</li>
    <li class="address"><svg viewBox="0 0 24 24"><path d="M12 1a8 8 0 0 0-8 8c0 6 8 14 8 14s8-8 8-14a8 8 0 0 0-8-8zm0 11a3 3 0 1 1 0-6 3 3 0 0 1 0 6z"/></svg><span>Unit 4, 517 Wattlebrook Lane,<br>Kemberly NSW 2893</span></li>
  </ul>

  <div class="brand" style="left:862px;top:0px">
    <div class="brand__mark" style="background:var(--orange);margin-top:10px"></div>
    <p class="brand__name" style="color:var(--orange)">MIVROTEL HAVEN</p>
  </div>
  <p class="tagline" style="left:827px;top:138px;width:270px;height:44px;padding-top:5px;text-align:center;background:var(--orange);color:var(--white)">Specialist Provider of Multicultural<br>Support Services</p>

  <div class="social" style="left:42px;top:318px;color:var(--ink)">
    <span class="social__menu"></span>
    <span class="social__item"></span><span class="social__item"></span><span class="social__item"></span><span class="social__item"></span>
  </div>
</section>

</body>
</html>
```